Corvane semiconductor corporate presentation

We need a new template with some fresh design elements as we've just announced the acquisition of a new company. Similarly, the backend of the ppt is not set up correctly - and doesn't format properly when dropping in copied text. Attached is the powerpoint presentation/ template as it stands today.
Industry/Entity Type
It Company
Font styles to use
Other font styles liked:
- Arial
Look and feel
Each slider illustrates characteristics of the customer's brand and the style your logo design should communicate.

```html
<!DOCTYPE html>
<html lang="en">
<head>
<meta charset="utf-8">
<title>Corvane semiconductor – Diverse Product Portfolio</title>
<link rel="stylesheet" href="https://fonts.googleapis.com/css2?family=Arimo:wght@400;700&display=swap">
<style>
  :root {
    --brand-blue: #0b56a6;
    --title-blue: #1d5aa8;
    --deep-blue: #0a4c94;
    --brand-green: #9cc63b;
    --muted-green: #8cb36a;
    --icon-green: #a9d34a;
    --text-grey: #4d4d4d;
    --white: #ffffff;
    --page: #ffffff;
  }
  * { margin: 0; padding: 0; box-sizing: border-box; }
  html, body { width: 1200px; height: 831px; overflow: hidden; background: var(--page); }
  body { font-family: "Arimo", Arial, sans-serif; color: var(--text-grey); }
  .slide { position: relative; width: 1200px; height: 831px; overflow: hidden; background: var(--page); }

  .slide-title {
    position: absolute; left: 44px; top: 44px;
    font-size: 41px; line-height: 44px; font-weight: 400; color: var(--title-blue);
  }
  .slide-subtitle {
    position: absolute; left: 44px; top: 152px;
    font-size: 24px; color: var(--text-grey);
  }

  .band {
    position: absolute; left: 46px; right: 0;
    background: var(--brand-blue);
  }
  .band-products { top: 427px; height: 135px; }
  .band-value { top: 586px; height: 135px; }

  .row-badge {
    position: absolute; left: 6px; width: 127px; height: 127px; border-radius: 50%;
    background: var(--brand-green); color: var(--text-grey);
    display: flex; align-items: center; justify-content: center; text-align: center;
    font-size: 21px; line-height: 27px; z-index: 3;
  }
  .badge-products { top: 431px; }
  .badge-value { top: 590px; }

  .column { position: absolute; top: 0; width: 133px; height: 831px; }
  .column-label {
    position: absolute; top: 196px; left: -40px; width: 213px; text-align: center;
    font-size: 22px; line-height: 29px; color: var(--text-grey);
  }
  .column-label.single { top: 210px; }
  .column-stem {
    position: absolute; left: 0; top: 330px; width: 133px; height: 97px;
    background: linear-gradient(180deg, #1a5ea8 0%, var(--deep-blue) 100%);
  }
  .column-icon {
    position: absolute; left: 0; top: 257px; width: 133px; height: 133px;
  }
  .column-cell {
    position: absolute; left: -40px; width: 213px; height: 135px;
    display: flex; align-items: center; justify-content: center; text-align: center;
    color: var(--white); font-size: 20px; line-height: 30px;
  }
  .cell-products { top: 427px; }
  .cell-value { top: 586px; line-height: 28px; }
  .connector {
    position: absolute; left: 0; width: 133px; background: var(--muted-green);
  }
  .connector-mid { top: 562px; height: 24px; }
  .connector-low { top: 721px; height: 19px; background: var(--brand-green); }

  .footer {
    position: absolute; left: 0; right: 0; top: 753px; height: 78px;
    background: var(--brand-green);
  }
  .footer-note {
    position: absolute; left: 0; right: 0; top: 33px; text-align: center;
    font-size: 17px; color: var(--text-grey);
  }
  .page-number { position: absolute; right: 48px; top: 28px; font-size: 17px; color: var(--text-grey); }
</style>
</head>
<body>
<main class="slide">
  <h1 class="slide-title">Diverse Product<br>Portfolio</h1>
  <p class="slide-subtitle">Powering efficient, smart connected devices</p>

  <svg width="0" height="0" style="position:absolute">
    <defs>
      <radialGradient id="icon-fill" cx="50%" cy="50%" r="50%">
        <stop offset="0%" stop-color="#a9d34a"/>
        <stop offset="45%" stop-color="#6fae4a"/>
        <stop offset="100%" stop-color="#1b5ea6"/>
      </radialGradient>
    </defs>
  </svg>

  <div class="band band-products"></div>
  <div class="band band-value"></div>
  <div class="row-badge badge-products">Products:</div>
  <div class="row-badge badge-value">Corvane<br>Value:</div>

  <!-- Power Management -->
  <section class="column" style="left:182px">
    <div class="column-label">Power<br>Management</div>
    <div class="column-stem"></div>
    <svg class="column-icon" viewBox="0 0 133 133">
      <circle cx="66.5" cy="66.5" r="64" fill="url(#icon-fill)" stroke="#fff" stroke-width="3"/>
      <rect x="50" y="32" width="33" height="68" rx="5" fill="none" stroke="#fff" stroke-width="5"/>
      <rect x="59" y="26" width="15" height="6" fill="#fff"/>
      <rect x="56" y="40" width="21" height="13" fill="#fff"/>
      <rect x="56" y="59" width="21" height="13" fill="#fff"/>
      <rect x="56" y="78" width="21" height="13" fill="#fff"/>
    </svg>
    <div class="column-cell cell-products">PMICs,Chargers<br>Wireless<br>Charging</div>
    <div class="connector connector-mid"></div>
    <div class="column-cell cell-value">Integration,<br>Efficiency, Size,<br>Flexibility</div>
    <div class="connector connector-low"></div>
  </section>

  <!-- Wireless Connectivity -->
  <section class="column" style="left:382px">
    <div class="column-label">Wireless<br>Connectivity</div>
    <div class="column-stem"></div>
    <svg class="column-icon" viewBox="0 0 133 133">
      <circle cx="66.5" cy="66.5" r="64" fill="url(#icon-fill)" stroke="#fff" stroke-width="3"/>
      <g stroke="#fff" stroke-width="4" fill="none">
        <polygon points="66,32 96,49 96,84 66,101 36,84 36,49"/>
        <line x1="66" y1="66" x2="96" y2="49"/>
        <line x1="66" y1="66" x2="51" y2="84"/>
      </g>
      <g fill="#fff">
        <circle cx="66" cy="32" r="7"/><circle cx="96" cy="49" r="7"/><circle cx="96" cy="84" r="7"/>
        <circle cx="66" cy="101" r="7"/><circle cx="36" cy="84" r="7"/><circle cx="36" cy="49" r="7"/>
        <circle cx="66" cy="66" r="6"/>
      </g>
    </svg>
    <div class="column-cell cell-products">Bluewave<br>DECT</div>
    <div class="connector connector-mid"></div>
    <div class="column-cell cell-value">Performance<br>&amp; Battery Life</div>
    <div class="connector connector-low"></div>
  </section>

  <!-- Audio -->
  <section class="column" style="left:569px">
    <div class="column-label single">Audio</div>
    <div class="column-stem"></div>
    <svg class="column-icon" viewBox="0 0 133 133">
      <circle cx="66.5" cy="66.5" r="64" fill="url(#icon-fill)" stroke="#fff" stroke-width="3"/>
      <g stroke="#fff" stroke-width="4.5" fill="none" stroke-linejoin="round" stroke-linecap="round">
        <rect x="33" y="53" width="12" height="27" rx="3"/>
        <polygon points="45,53 68,36 68,97 45,80"/>
        <path d="M77 52 Q84 66.5 77 81"/>
        <path d="M86 44 Q98 66.5 86 89"/>
      </g>
    </svg>
    <div class="column-cell cell-products">Codecs, Amplifiers,<br>Processors</div>
    <div class="connector connector-mid"></div>
    <div class="column-cell cell-value">Audio Quality<br>&amp; Battery Life</div>
    <div class="connector connector-low"></div>
  </section>

  <!-- Power Conversion -->
  <section class="column" style="left:754px">
    <div class="column-label">Power<br>Conversion</div>
    <div class="column-stem"></div>
    <svg class="column-icon" viewBox="0 0 133 133">
      <circle cx="66.5" cy="66.5" r="64" fill="url(#icon-fill)" stroke="#fff" stroke-width="3"/>
      <g stroke="#fff" stroke-width="5" fill="none" stroke-linecap="round">
        <path d="M55 38 A20 20 0 1 0 78 38"/>
        <line x1="66.5" y1="29" x2="66.5" y2="54"/>
      </g>
      <circle cx="46" cy="95" r="7" fill="#fff"/>
      <circle cx="66.5" cy="95" r="7" fill="#fff" opacity="0.75"/>
      <circle cx="87" cy="95" r="7" fill="#fff" opacity="0.5"/>
    </svg>
    <div class="column-cell cell-products">AC/DC<br>Converters</div>
    <div class="connector connector-mid"></div>
    <div class="column-cell cell-value">Power<br>Efficiency,<br>Size,&nbsp; BOM<br>Cost</div>
    <div class="connector connector-low"></div>
  </section>

  <!-- Lighting -->
  <section class="column" style="left:925px">
    <div class="column-label single">Lighting</div>
    <div class="column-stem"></div>
    <svg class="column-icon" viewBox="0 0 133 133">
      <circle cx="66.5" cy="66.5" r="64" fill="url(#icon-fill)" stroke="#fff" stroke-width="3"/>
      <circle cx="66.5" cy="66.5" r="16" fill="none" stroke="#fff" stroke-width="3.5"/>
      <circle cx="66.5" cy="66.5" r="10" fill="#c7e36b" stroke="#fff" stroke-width="2"/>
      <g stroke="#fff" stroke-width="3.5" stroke-linecap="round">
        <line x1="66.5" y1="30" x2="66.5" y2="42"/><line x1="66.5" y1="91" x2="66.5" y2="103"/>
        <line x1="30" y1="66.5" x2="42" y2="66.5"/><line x1="91" y1="66.5" x2="103" y2="66.5"/>
        <line x1="41" y1="41" x2="49" y2="49"/><line x1="84" y1="84" x2="92" y2="92"/>
        <line x1="92" y1="41" x2="84" y2="49"/><line x1="49" y1="84" x2="41" y2="92"/>
      </g>
    </svg>
    <div class="column-cell cell-products">LED<br>Drivers</div>
    <div class="connector connector-mid"></div>
    <div class="column-cell cell-value">Power Efficiency,<br>Size,&nbsp; BOM Cost</div>
    <div class="connector connector-low"></div>
  </section>

  <footer class="footer">
    <p class="footer-note">© 2017 Corvane semiconductor</p>
    <span class="page-number">6</span>
  </footer>
</main>
</body>
</html>
```